Banner for homepage

It is a new banner for the homepage, temporary site address is 61.187.40.72 ( is the biggest banner only ) . Would be 5 variations for image content as below (in Portuguese ) :

Image 1:
Leitor de codigo de barras
Todos os tipos de leitores de código de barras para as mais diversas aplicações.
( example of product images in : http://www.quentorlabs.com/en-US/Pages/Category.aspx?category=barcode-scanners&cat=KLT)

Image 2:
Impressora de etiquetas
Identifique o que for nessário com o melhor custo/beneficio e flexibilidade de materiais de impressão.
( example of product images in : vintor.com in label printers desktop and industrial)

Image 3:
Impressora de cupom
Imprima recibos e cupons fiscais com agilidade e qualidade, temos a impressora certa para o seu PDV.
( example of product images in : http://www.palutrek.com.br/equipamento-categoria-impressoras+fiscais.html)

Image 4:
Coletor de dados
Computadores móveis com leitor de código de barras, que levam a automação para frente de trabalho.
( example of product images in : http://www.quentorlabs.com/en-US/Pages/Category.aspx?cat=KLT&category=hand-held-mobile-computer)

Image 5:
Etiquetas e Ribbons:
Etiquetas adesivas e não adesivas em vários de tipos de materiais, papéis e plásticos. O ribbon certo para impressão perfeita em cada material.
( example of product images in : http://www.tagmirelo.com/cats/supplies/barcode-printer.htm?nav=hdr)

```html
<!DOCTYPE html>
<html lang="pt-BR">
<head>
<meta charset="utf-8">
<title>Corvalto — Soluções em Automação e Código de barras</title>
<link rel="stylesheet" href="https://fonts.googleapis.com/css2?family=Oswald:wght@300;400;500;700&family=Open+Sans:wght@400;600;700&display=swap">
<style>
  :root {
    --red-top: #d23a40;
    --red-base: #c2303a;
    --page-bg: #ececec;
    --nav-top: #545454;
    --nav-bottom: #2f2f2f;
    --white: #ffffff;
    --ink: #2b2b2b;
    --accent-orange: #ee5a24;
    --hero-red-light: #b8323a;
    --hero-red-dark: #8e1f27;
    --hero-yellow: #ffef0a;
    --hero-copy: #f2a27a;
    --btn-orange-top: #f29a2e;
    --btn-orange-bottom: #c8650f;
    --card-dark-top: #3a3a3a;
    --card-dark-bottom: #1e1e1e;
    --card-grey-top: #9c9690;
    --card-grey-bottom: #6f6a66;
    --tan: #d8b78a;
    --btn-red-top: #e2413f;
    --btn-red-bottom: #b51e1e;
  }
  * { box-sizing: border-box; margin: 0; padding: 0; }
  html, body { width: 1200px; height: 568px; overflow: hidden; }
  body {
    position: relative;
    background: var(--page-bg);
    font-family: "Open Sans", Arial, sans-serif;
    color: var(--ink);
  }

  /* Header band */
  .site-header {
    position: absolute; left: 0; top: 0; width: 1200px; height: 128px;
    background: linear-gradient(180deg, var(--red-top), var(--red-base));
  }
  .brand { position: absolute; left: 60px; top: 12px; width: 310px; }
  .brand-name {
    display: block; text-align: center;
    font-family: "Oswald", sans-serif; font-weight: 700;
    font-size: 38px; letter-spacing: 6px; line-height: 48px;
    color: var(--white);
  }
  .brand-tagline {
    display: block; text-align: center; margin-top: 7px;
    font-size: 12.5px; color: var(--white);
  }
  .utility-links {
    position: absolute; right: 80px; top: 12px;
    display: flex; list-style: none;
    font-size: 13.5px; font-weight: 600; color: var(--white);
  }
  .utility-links li { padding: 0 12px; border-left: 1px solid rgba(255,255,255,.6); line-height: 16px; }
  .utility-links li:first-child { border-left: none; }
  .utility-links li:last-child { padding-right: 0; }

  .contact-box {
    position: absolute; top: 41px; height: 50px; background: var(--white);
    padding: 6px 12px; box-shadow: 0 1px 3px rgba(0,0,0,.25);
    font-family: "Oswald", sans-serif;
  }
  .contact-box .label { display: block; font-size: 16px; font-weight: 400; color: var(--ink); line-height: 20px; }
  .contact-box .sub { display: block; font-size: 12px; color: var(--accent-orange); line-height: 18px; }
  .contact-chat { left: 833px; width: 119px; }
  .contact-phones { left: 969px; width: 154px; }
  .contact-phones .caret { position: absolute; right: 10px; top: 21px; }

  /* Main navigation */
  .main-nav {
    position: absolute; left: 31px; top: 102px; width: 1114px; height: 47px;
    background: linear-gradient(180deg, var(--nav-top), var(--nav-bottom));
    border-radius: 3px; box-shadow: 0 2px 3px rgba(0,0,0,.3);
  }
  .main-nav ul { display: flex; list-style: none; height: 47px; padding-left: 2px; }
  .main-nav li {
    font-family: "Oswald", sans-serif; font-weight: 400; font-size: 13px;
    color: var(--white); line-height: 47px; padding: 0 13px;
    border-right: 1px solid #222; box-shadow: 1px 0 0 #5e5e5e;
    text-transform: uppercase; white-space: nowrap;
  }
  .main-nav li:last-child { border-right: none; box-shadow: none; }
  .search-field {
    position: absolute; left: 939px; top: 11px; width: 167px; height: 27px;
    background: #2c2c2c; border: 1px solid #1c1c1c; border-radius: 3px;
    box-shadow: inset 0 1px 2px rgba(0,0,0,.6);
    font-size: 13px; color: #d6d6d6; line-height: 25px; padding-left: 8px;
  }
  .search-field svg { position: absolute; right: 7px; top: 6px; }

  /* Hero banner */
  .hero {
    position: absolute; left: 53px; top: 171px; width: 798px; height: 365px;
    border-radius: 7px; overflow: hidden;
    background: radial-gradient(ellipse at 40% 40%, var(--hero-red-light), var(--hero-red-dark) 85%);
    box-shadow: 0 2px 6px rgba(0,0,0,.25);
  }
  .hero-product {
    position: absolute; left: 32px; top: 85px; width: 222px; height: 188px;
    border-radius: 6px;
    background: linear-gradient(180deg, #9a9a9a, #3a3a3a);
  }
  .hero-title {
    position: absolute; left: 276px; top: 42px;
    font-family: "Oswald", sans-serif; font-weight: 300; font-size: 54px;
    color: var(--white); line-height: 64px; letter-spacing: -.5px; white-space: nowrap;
  }
  .hero-headline {
    position: absolute; left: 276px; top: 108px;
    font-family: "Oswald", sans-serif; font-weight: 700; font-size: 70px;
    color: var(--hero-yellow); line-height: 86px; letter-spacing: .5px; white-space: nowrap;
  }
  .hero-copy {
    position: absolute; left: 276px; top: 204px; width: 490px;
    font-family: "Oswald", sans-serif; font-weight: 300; font-size: 20.5px;
    color: var(--hero-copy); line-height: 26px;
  }
  .hero-cta {
    position: absolute; left: 587px; top: 286px; width: 165px; height: 37px;
    border-radius: 5px; text-align: center;
    background: linear-gradient(180deg, var(--btn-orange-top), var(--btn-orange-bottom));
    box-shadow: 0 2px 3px rgba(0,0,0,.4);
    font-family: "Oswald", sans-serif; font-size: 18px; color: var(--white); line-height: 37px;
  }

  /* Side promo cards */
  .promo-card {
    position: absolute; left: 876px; width: 250px; height: 173px;
    border-radius: 4px; overflow: hidden;
    box-shadow: 0 1px 4px rgba(0,0,0,.35);
  }
  .promo-delivery { top: 173px; background: linear-gradient(180deg, var(--card-dark-top), var(--card-dark-bottom)); }
  .promo-invoice { top: 362px; background: linear-gradient(180deg, var(--card-grey-top), var(--card-grey-bottom)); }
  .promo-title {
    position: absolute; left: 26px; top: 22px; white-space: nowrap;
    font-family: "Oswald", sans-serif; font-weight: 500; font-size: 33px; line-height: 40px; letter-spacing: -.3px;
  }
  .promo-delivery .promo-title .first { color: var(--tan); }
  .promo-delivery .promo-title .second { color: var(--white); }
  .promo-invoice .promo-title { left: 25px; }
  .promo-invoice .promo-title .first { color: #2a2a2a; }
  .promo-invoice .promo-title .second { color: var(--white); }
  .promo-text {
    position: absolute; left: 26px; top: 68px; width: 160px; z-index: 2;
    font-size: 12.5px; line-height: 19px; color: var(--white);
  }
  .promo-btn {
    position: absolute; left: 25px; top: 121px; width: 100px; height: 27px; z-index: 2;
    border-radius: 14px; text-align: center;
    font-family: "Oswald", sans-serif; font-size: 14px; line-height: 27px; color: var(--white);
    box-shadow: 0 1px 2px rgba(0,0,0,.5);
  }
  .promo-delivery .promo-btn { background: linear-gradient(180deg, #e6cc9f, #b8935e); }
  .promo-invoice .promo-btn { background: linear-gradient(180deg, var(--btn-red-top), var(--btn-red-bottom)); }
  .promo-art { position: absolute; border-radius: 4px; z-index: 1; }
  .promo-delivery .promo-art { left: 152px; top: 82px; width: 92px; height: 80px; background: linear-gradient(160deg, #e0954a, #8a4d1c); }
  .promo-invoice .promo-art { left: 146px; top: 80px; width: 78px; height: 88px; background: linear-gradient(180deg, #2f4a4a, #132020); }
</style>
</head>
<body>

<header class="site-header">
  <div class="brand">
    <span class="brand-name">CORVALTO</span>
    <span class="brand-tagline">Soluções em Automação e Código de barras</span>
  </div>

  <ul class="utility-links">
    <li>Principal</li>
    <li>Quem Somos</li>
    <li>Entre em Contato</li>
  </ul>

  <div class="contact-box contact-chat">
    <span class="label">CHAT ONLINE</span>
    <span class="sub">CLIQUE AQUI</span>
  </div>
  <div class="contact-box contact-phones">
    <span class="label">TELEFONES</span>
    <span class="sub">TODOS OS ESTADOS</span>
    <svg class="caret" width="9" height="6" viewBox="0 0 9 6"><path d="M0 0h9L4.5 6z" fill="#555"/></svg>
  </div>

  <nav class="main-nav">
    <ul>
      <li>Leitor de código de barras</li>
      <li>Impressora de etiquetas</li>
      <li>Automação comercial</li>
      <li>Etiquetas</li>
      <li>Coletor de dados</li>
      <li>Impressora de cartão</li>
      <li>Marcas</li>
    </ul>
    <div class="search-field">Busca
      <svg width="13" height="13" viewBox="0 0 13 13"><circle cx="5" cy="5" r="3.8" fill="none" stroke="#e0e0e0" stroke-width="1.8"/><path d="M8 8l4 4" stroke="#e0e0e0" stroke-width="2.2" stroke-linecap="round"/></svg>
    </div>
  </nav>
</header>

<section class="hero">
  <div class="hero-product" role="img" aria-label="Foto de impressora industrial de etiquetas imprimindo uma etiqueta"></div>
  <h1 class="hero-title">Impressora de Etiquetas</h1>
  <p class="hero-headline">Identifique o que</p>
  <p class="hero-copy">Identifique o que for nessário com o melhor custo/beneficio e flexibilidade de materiais de impressão.</p>
  <div class="hero-cta">Veja Mais</div>
</section>

<aside class="promo-card promo-delivery">
  <h2 class="promo-title"><span class="first">Entrega</span><span class="second">Rápida</span></h2>
  <p class="promo-text">Enviamos sua compra para todo o Brasil.</p>
  <div class="promo-art" role="img" aria-label="Ilustração de caixa de papelão aberta"></div>
  <div class="promo-btn">Leia Mais</div>
</aside>

<aside class="promo-card promo-invoice">
  <h2 class="promo-title"><span class="first">Boleto</span><span class="second">Faturado</span></h2>
  <p class="promo-text">Receba seu pedido com os boletos.</p>
  <div class="promo-art" role="img" aria-label="Ilustração de sacola de compras escura"></div>
  <div class="promo-btn">Leia Mais</div>
</aside>

</body>
</html>
```